Dunmore Plumbing LLC business card

Would like a modern looking business card with my new logo

Contact Information for Business Card

Calvin Dunmore 2418 Elm Hollow Rd Oakridge Falls, NH 06999, Dunmoreplumbingllc@exampletrade.com, 203-555-0174

```html
<!DOCTYPE html>
<html lang="en">
<head>
<meta charset="utf-8">
<title>Dunmore Plumbing LLC — Business Card</title>
<link rel="stylesheet" href="https://fonts.googleapis.com/css2?family=Montserrat:wght@400;500;700;800&display=swap">
<style>
  :root {
    --bg: #d3d6d7;
    --paper: #f4f4f4;
    --ink: #1a1a1a;
    --text: #2b2b2b;
    --blue: #2a9ad8;
    --rule: #555555;
    --faint: #e6e6e6;
  }
  * { box-sizing: border-box; margin: 0; padding: 0; }
  html, body { width: 1200px; height: 905px; overflow: hidden; }
  body {
    background: var(--bg);
    font-family: "Montserrat", Arial, sans-serif;
    display: flex;
    align-items: center;
    justify-content: center;
    gap: 40px;
  }
  .card {
    position: relative;
    width: 540px;
    height: 309px;
    background: var(--paper);
    box-shadow: 0 10px 28px rgba(0,0,0,0.18);
    overflow: hidden;
  }
  .brand-name {
    display: flex; align-items: center; gap: 8px;
    font-weight: 800; color: var(--ink);
    text-transform: uppercase; line-height: 1.05;
  }
  .brand-square { width: 14px; height: 14px; background: var(--blue); flex: none; }

  /* Front */
  .card-front .brand {
    position: absolute;
    left: 30px; top: 88px;
    width: 200px;
  }
  .card-front .brand-name { font-size: 21px; }
  .divider {
    position: absolute; left: 244px; top: 70px;
    width: 1px; height: 150px; background: var(--rule);
  }
  .contact { position: absolute; left: 264px; top: 72px; right: 12px; }
  .contact-name {
    color: var(--blue); font-weight: 800; font-size: 22px;
    text-transform: uppercase; letter-spacing: 0.5px; margin-bottom: 10px;
    white-space: nowrap;
  }
  .contact-address { font-size: 12.5px; color: var(--text); line-height: 1.35; margin-bottom: 8px; }
  .contact-line {
    display: flex; align-items: center; gap: 6px;
    font-size: 11px; color: var(--text); line-height: 1.7; white-space: nowrap;
  }
  .contact-line svg { width: 11px; height: 11px; flex: none; fill: var(--blue); }
  .band-rule { position: absolute; left: 0; right: 0; bottom: 34px; height: 2px; background: var(--blue); }
  .band { position: absolute; left: 0; right: 0; bottom: 0; height: 28px; background: var(--ink); }

  /* Back */
  .card-back .decoration {
    position: absolute; left: 40px; top: 70px;
    width: 130px; height: 170px;
    background: radial-gradient(ellipse at center, var(--faint) 0%, rgba(230,230,230,0) 70%);
  }
  .card-back .brand {
    position: absolute; inset: 0;
    display: flex; align-items: center; justify-content: center;
  }
  .card-back .brand-name { font-size: 34px; gap: 12px; }
  .card-back .brand-square { width: 20px; height: 20px; }
</style>
</head>
<body>
  <section class="card card-front" aria-label="Business card front">
    <div class="brand">
      <div class="brand-name"><span class="brand-square"></span><span>Dunmore Plumbing LLC</span></div>
    </div>
    <div class="divider"></div>
    <div class="contact">
      <h1 class="contact-name">Calvin Dunmore</h1>
      <p class="contact-address">2418 Elm Hollow Rd<br>Oakridge Falls, NH 06999</p>
      <p class="contact-line">
        <svg viewBox="0 0 24 24" aria-hidden="true"><path d="M6.6 10.8a15 15 0 0 0 6.6 6.6l2.2-2.2a1 1 0 0 1 1-.25 11.4 11.4 0 0 0 3.6.6 1 1 0 0 1 1 1V20a1 1 0 0 1-1 1A17 17 0 0 1 3 4a1 1 0 0 1 1-1h3.5a1 1 0 0 1 1 1c0 1.25.2 2.45.6 3.6a1 1 0 0 1-.25 1z"/></svg>
        203-555-0174
      </p>
      <p class="contact-line">
        <svg viewBox="0 0 24 24" aria-hidden="true"><path d="M2 5h20v14H2z M3.5 6.5 12 13l8.5-6.5" stroke="#f4f4f4" stroke-width="1.5"/></svg>
        Dunmoreplumbingllc@exampletrade.com
      </p>
      <p class="contact-line">
        <svg viewBox="0 0 24 24" aria-hidden="true"><circle cx="12" cy="12" r="10"/><path d="M2 12h20M12 2c3 3 3 17 0 20M12 2c-3 3-3 17 0 20" stroke="#f4f4f4" stroke-width="1.3" fill="none"/></svg>
        www.dunmoreplumbingllc.example
      </p>
    </div>
    <div class="band-rule"></div>
    <div class="band"></div>
  </section>

  <section class="card card-back" aria-label="Business card back">
    <div class="decoration" role="img" aria-label="Faint background illustration of a water tap"></div>
    <div class="brand">
      <div class="brand-name"><span class="brand-square"></span><span>Dunmore Plumbing LLC</span></div>
    </div>
  </section>
</body>
</html>
```